Harbor Crest Solutions Letterhead Design

The project name sums it up. Just need a professional letterhead design / template we can use in our marketing folders.

Here's the address / contact info for the letterhead: Harbor Crest Solutions 4817 Maple Ridge Dr Suite 150 Millbrook, Vermont 05419 555-508-7364 www.harborcrestsolutions.us support@harborcrestsolutions.us

```html
<!DOCTYPE html>
<html lang="en">
<head>
<meta charset="utf-8">
<title>Harbor Crest Solutions Letterhead</title>
<link href="https://fonts.googleapis.com/css2?family=Open+Sans:wght@400&family=Orbitron:wght@700;800&display=swap" rel="stylesheet">
<style>
  :root {
    --brand-blue: #1f4f9e;
    --ink: #2b2b2b;
    --navy: #111a33;
    --rule-grey: #b9bcc2;
    --paper: #ffffff;
    --backdrop: #e9e7e3;
    --faint: #ececec;
  }
  html, body {
    margin: 0;
    width: 1200px;
    height: 900px;
    overflow: hidden;
    background: var(--backdrop);
  }
  .letterhead {
    position: absolute;
    left: 267px;
    top: 21px;
    width: 665px;
    height: 857px;
    background: var(--paper);
    overflow: hidden;
    box-shadow: 0 2px 10px rgba(0,0,0,0.12);
    font-family: "Open Sans", Arial, sans-serif;
  }
  .brand-mark {
    position: absolute;
    left: 32px;
    top: 62px;
    display: flex;
    align-items: center;
    gap: 10px;
  }
  .brand-mark__square {
    width: 34px;
    height: 34px;
    background: var(--brand-blue);
  }
  .brand-mark__name {
    font-family: "Orbitron", Arial, sans-serif;
    font-weight: 800;
    font-size: 17px;
    line-height: 1.1;
    color: var(--brand-blue);
    letter-spacing: 0.5px;
  }
  .contact-block {
    position: absolute;
    left: 440px;
    top: 34px;
    color: var(--ink);
    font-size: 10.6px;
    line-height: 14px;
  }
  .contact-block__company {
    font-family: "Orbitron", Arial, sans-serif;
    font-weight: 700;
    font-size: 8.6px;
    letter-spacing: 0.6px;
    text-transform: uppercase;
    color: var(--brand-blue);
    margin-bottom: 1px;
  }
  .contact-block__address { margin: 0 0 7px; }
  .contact-line {
    display: flex;
    align-items: center;
    gap: 5px;
  }
  .contact-line svg { width: 11px; height: 11px; fill: var(--brand-blue); flex: none; }
  .faint-emblem {
    position: absolute;
    left: -40px;
    top: 672px;
    width: 176px;
    height: 176px;
    border-radius: 50%;
    background: var(--faint);
  }
  .certification-badge {
    position: absolute;
    left: 524px;
    top: 792px;
    width: 111px;
    height: 32px;
    border: 2px solid var(--brand-blue);
    border-radius: 16px;
    box-sizing: border-box;
  }
  .footer-rule {
    position: absolute;
    left: 0; right: 0;
    top: 841px;
    height: 2px;
    background: var(--rule-grey);
  }
  .footer-band {
    position: absolute;
    left: 0; right: 0;
    top: 845px;
    height: 12px;
    background: var(--navy);
  }
</style>
</head>
<body>
  <main class="letterhead">
    <div class="brand-mark">
      <span class="brand-mark__square"></span>
      <span class="brand-mark__name">HARBOR CREST<br>SOLUTIONS</span>
    </div>

    <section class="contact-block">
      <div class="contact-block__company">Harbor Crest Solutions</div>
      <p class="contact-block__address">4817 Maple Ridge Dr Suite 150<br>Millbrook, Vermont 05419</p>
      <div class="contact-line">
        <svg viewBox="0 0 24 24" aria-hidden="true"><path d="M6.6 10.8a15.1 15.1 0 0 0 6.6 6.6l2.2-2.2c.3-.3.7-.4 1-.2 1.1.4 2.3.6 3.6.6.6 0 1 .4 1 1V20c0 .6-.4 1-1 1A17 17 0 0 1 3 4c0-.6.4-1 1-1h3.5c.6 0 1 .4 1 1 0 1.3.2 2.5.6 3.6.1.3 0 .7-.2 1z"/></svg>
        <span>555-508-7364</span>
      </div>
      <div class="contact-line">
        <svg viewBox="0 0 24 24" aria-hidden="true"><path d="M2 6.5V19h20V6.5l-10 7z"/><path d="M2 5h20l-10 7z"/></svg>
        <span>support@harborcrestsolutions.us</span>
      </div>
      <div class="contact-line">
        <svg viewBox="0 0 24 24" aria-hidden="true"><path d="M12 2a10 10 0 1 0 0 20 10 10 0 0 0 0-20zm-1 17.9A8 8 0 0 1 4.1 11H8c.1 3 .9 6.1 3 8.9zm0-10.9H8.1c.2-2.4 1-4.6 2.9-6.9V9zm2-6.9c1.9 2.3 2.7 4.5 2.9 6.9H13zm0 8.9h2.9c-.2 2.6-1 5.2-2.9 7.9zm2.3 8.4c1.4-2.5 2.1-5.3 2.6-8.4h2A8 8 0 0 1 15.3 19.4zM17.9 9c-.2-2.3-.9-4.4-2.1-6.4A8 8 0 0 1 19.9 9z"/></svg>
        <span>www.harborcrestsolutions.us</span>
      </div>
    </section>

    <div class="faint-emblem" aria-hidden="true"></div>
    <div class="certification-badge" role="img" aria-label="Veteran owned business certification badge"></div>

    <div class="footer-rule"></div>
    <div class="footer-band"></div>
  </main>
</body>
</html>
```